Flyer-Design für Physiotherapie-Praxis
Zielgruppe
Wir sind eine Praxis für Physiotherapie und möchten durch diesen Flyer neue Patienten werben. Der Flyer soll in Arztpraxen ausliegen und dort den Patienten direkt ansprechen und auf uns aufmerksam machen. Es ist auch eine Verknüpfung der Therapie mit einem Training in einem Gesundheitsstudio möglich, da im gleichen Haus das Kraftwerk Sonnhalde Lindmoos beheimatet ist.
Aufgabenstellung
Der Fokus auf unsere Prinzipien (Ganzheitliche Therapie, hohes Maß an Therapiemöglichkeiten, Variation in den therapeutischen Ansätzen durch unterschiedlich fortgebildete Therapeuten, die nach den gleichen Idealen arbeiten)

```html
<!DOCTYPE html>
<html lang="de">
<head>
<meta charset="utf-8">
<title>Physiotherapie-Praxis – Flyer</title>
<link href="https://fonts.googleapis.com/css2?family=Open+Sans:wght@400;700;800&display=swap" rel="stylesheet">
<style>
  :root {
    --accent: #2aa8ec;
    --text: #161616;
    --paper: #ffffff;
  }
  * { margin: 0; padding: 0; box-sizing: border-box; }
  html, body { width: 776px; height: 1200px; overflow: hidden; background: var(--paper); }
  .flyer {
    position: relative; width: 776px; height: 1200px; overflow: hidden;
    font-family: "Open Sans", Arial, sans-serif; color: var(--text);
  }
  .headline {
    position: absolute; left: 0; top: 14px; width: 378px;
    text-align: center; color: var(--accent);
    font-weight: 800; font-size: 33px; line-height: 33px; letter-spacing: 0.14em;
  }
  .intro {
    position: absolute; left: 5px; top: 153px; width: 378px;
    font-size: 18.4px; line-height: 18.7px; white-space: nowrap;
  }
  .subhead {
    position: absolute; left: 0; width: 366px; text-align: center;
    color: var(--accent); font-weight: 700; font-size: 27px; line-height: 38px;
  }
  .subhead--therapy { top: 505px; }
  .therapy-text {
    position: absolute; left: 7px; top: 579px; width: 378px;
    font-size: 18.6px; line-height: 21.6px; white-space: nowrap; letter-spacing: 0.01em;
  }
  .subhead--training {
    top: 843px; left: 6px; width: auto; text-align: left;
    font-size: 26px; line-height: 36px; letter-spacing: -0.09em; font-weight: 800;
  }
  .training-text {
    position: absolute; left: 5px; top: 884px; width: 770px;
    font-size: 18px; line-height: 20.3px; white-space: nowrap;
  }
  .training-text .gap { display: block; height: 3px; }
  .photo { position: absolute; left: 382px; width: 384px; }
  .photo--therapist { top: 0; height: 248px; background: linear-gradient(135deg, #8a8f92 0%, #b9d4e2 45%, #e4e1da 100%); }
  .photo--handcasts { top: 265px; height: 248px; background: radial-gradient(ellipse at 50% 45%, #a9a9a9 0%, #5f5f5f 50%, #141414 100%); }
  .photo--massage { top: 529px; height: 249px; background: linear-gradient(135deg, #c98a5c 0%, #e0b08a 45%, #b97746 100%); }
  .photo--gym { top: 793px; height: 252px; background: linear-gradient(180deg, #f2f2ef 0%, #d9d9d6 50%, #8e8f90 100%); }
</style>
</head>
<body>
<div class="flyer">
  <h1 class="headline">WIR SIND<br>THERAPEUTEN<br>AUS<br>ÜBERZEUGUNG!</h1>

  <p class="intro">
    Unsere Praxis gibt es seit 1969.<br>
    In dieser Zeit konnten wir viel Erfahrung<br>
    sammeln.<br>
    Wir sind ein Team aus älteren und<br>
    jüngeren Therapeuten, aus Masseuren,<br>
    med. Bademeistern und<br>
    Physiotherapeuten. Diese bunte<br>
    Mischung beinhaltet viel Erfahrung und<br>
    viel Wissen.<br>
    Beides wird in regelmäßigen internen<br>
    Fortbildungen ausgetauscht.<br>
    So ergänzen wir uns gegenseitig.<br>
    Wir arbeiten als Team Hand in Hand<br>
    und schätzen das Fachwissen jedes<br>
    einzelnen Kollegen.<br>
    Wir sind motiviert und mit Freude bei<br>
    der Arbeit, denn wir wissen, was unsere<br>
    Patienten mit Hilfe der Physiotherapie<br>
    erreichen können.
  </p>

  <h2 class="subhead subhead--therapy">Vielezahl von<br>Therapiemöglichkeiten</h2>

  <p class="therapy-text">
    Wir haben eine Vielzahl von<br>
    Therapiegeräten und -hilfsmitteln zur<br>
    Verfügung, z.B. eine Kletterwand, Sling<br>
    Trainer, eine Vibrana®-Rüttelplatte,<br>
    einen Wippbalken und ein Bewegungsbad!<br>
    Im 32°C warmem Wasser können sich<br>
    unsere Patienten besser bewegen.<br>
    Mit unserem Fachwissen und unserer<br>
    Erfahrung haben wir uns auf die<br>
    Behandlung orthopädischer,<br>
    chirurgischer und neurologischer<br>
    Patienten spezialisiert.
  </p>

  <h2 class="subhead subhead--training">AKTIVES GESUNDHEITSTRAINING</h2>

  <p class="training-text">
    Für gute Fortschritte in der Therapie und<br>
    die Erhaltung dieser Fortschritte ist der<br>
    Weg zur sportlichen Aktivität essentiell.<br>
    Diesen Weg erleichtern wir unseren<br>
    Patienten durch unser Angebot des<br>
    Aktiven Gesundheitstrainings.<br>
    Zusätzlich zu Ihrem Rezept erhalten<br>
    unsere neuen Patienten einen<br>
    zusätzlichen und kostenfreien Beratungstermin im Kraftwerk Sonnhalde<br>
    Lindmoos. In diesem Termin zeigen wir Ihnen Möglichkeiten, selbst etwas zu<br>
    Ihrer Gesundung beizutragen.<span class="gap"></span>
    Je nachdem, was Ihnen gerade am effektivsten hilft, trainieren Sie 6 x am Kraft-<br>
    Ausdauer-Zirkel der Firma Ferrox oder am flexora-Zirkel. Das Training an diesen<br>
    Geräten ist einfach, sicher und effektiv. Da das Training maximal 35 Minuten Zeit<br>
    beansprucht ist Zeitmangel kein Argument mehr.
  </p>

  <div class="photo photo--therapist" role="img" aria-label="Foto: Therapeutin übt mit einem älteren Patienten an einem Trainingsgerät"></div>
  <div class="photo photo--handcasts" role="img" aria-label="Foto: silberne und goldene Handabgüsse des Teams mit Namenskärtchen"></div>
  <div class="photo photo--massage" role="img" aria-label="Foto: Hände bei einer Schultermassage"></div>
  <div class="photo photo--gym" role="img" aria-label="Foto: heller Trainingsraum mit Kraft- und Ausdauergeräten"></div>
</div>
</body>
</html>
```